Labels for an activated Charcoal Facial Wash, Scrub and Mask

We need a new label design for a new line of Facial products. The product, falls under our Brand Dovelin and is based on Activated Charcoal. Activated Black Charcoal Facial wash (250ml), Activated Black Charcoal Mask (100gms) and Activated Black Charcoal face scrub (100gms). We would like to see designs that are modern, clean and must communicate natural products.

```html
<!DOCTYPE html>
<html lang="en">
<head>
<meta charset="utf-8">
<title>Dovelin Activated Black Charcoal Facial Wash Labels</title>
<link href="https://fonts.googleapis.com/css2?family=Montserrat:wght@300;400;700&display=swap" rel="stylesheet">
<style>
  :root {
    --backdrop: #a3a585;
    --label-grey: #86878b;
    --label-grey-dark: #7a7b80;
    --label-white: #ffffff;
    --leaf-grey: #9a9b94;
    --leaf-white: #eef0e8;
    --charcoal: #0d0d0d;
    --ink-light: #ffffff;
    --ink-soft: #e4e4e4;
    --ink-muted: #8d8d8d;
    --brand-ink: #3a3a36;
    --brand-frame: #c9c6a4;
    --brand-tile: #ffffff;
  }
  * { box-sizing: border-box; margin: 0; padding: 0; }
  html, body { width: 1200px; height: 900px; overflow: hidden; }
  body {
    background: var(--backdrop);
    font-family: "Montserrat", sans-serif;
    display: flex;
    align-items: center;
    justify-content: center;
    gap: 90px;
  }
  .label {
    position: relative;
    width: 360px;
    height: 760px;
    display: flex;
    flex-direction: column;
    align-items: center;
    overflow: hidden;
  }
  .label--grey { background: linear-gradient(180deg, var(--label-grey) 0%, var(--label-grey-dark) 100%); }
  .label--white { background: var(--label-white); }

  .label__crimp {
    width: 100%;
    height: 14px;
    background: repeating-linear-gradient(90deg, rgba(0,0,0,.12) 0 1px, transparent 1px 4px);
  }
  .label__foliage {
    position: absolute;
    top: 14px; left: 0; right: 0;
    height: 230px;
  }
  .label--grey .label__foliage { background: linear-gradient(180deg, var(--leaf-grey) 0%, rgba(154,155,148,0) 100%); }
  .label--white .label__foliage { background: linear-gradient(180deg, var(--leaf-white) 0%, rgba(238,240,232,0) 100%); }

  .brand {
    position: relative;
    margin-top: 70px;
    width: 150px;
    height: 104px;
    background: var(--brand-tile);
    border: 1px solid var(--brand-frame);
    display: flex;
    align-items: center;
    justify-content: center;
    gap: 8px;
  }
  .brand__square { width: 9px; height: 9px; background: var(--brand-frame); }
  .brand__name {
    font-weight: 400;
    font-size: 17px;
    letter-spacing: 3px;
    color: var(--brand-ink);
    text-transform: uppercase;
  }

  .title-band {
    position: relative;
    width: 100%;
    margin-top: 46px;
    padding: 48px 0 60px;
    text-align: center;
  }
  .title-band__stroke {
    position: absolute;
    inset: 0 14px;
    background: var(--charcoal);
    border-radius: 6px;
  }
  .title-band__text { position: relative; display: inline-block; }
  .title__eyebrow {
    font-weight: 300;
    font-size: 19px;
    color: var(--ink-soft);
    letter-spacing: .5px;
  }
  .title__main {
    font-weight: 700;
    font-size: 31px;
    line-height: 1.05;
    color: var(--ink-light);
    margin-top: 8px;
  }
  .title__sub {
    font-weight: 300;
    font-size: 17px;
    letter-spacing: 4.5px;
    color: var(--ink-soft);
    border-top: 1px solid var(--ink-soft);
    margin-top: 8px;
    padding-top: 6px;
  }

  .claims {
    margin-top: 64px;
    text-align: center;
    list-style: none;
    font-weight: 400;
    font-size: 11px;
    letter-spacing: 3.5px;
    line-height: 2.3;
  }
  .label--grey .claims { color: var(--ink-soft); }
  .label--white .claims { color: var(--ink-muted); }

  .volume {
    margin-top: 40px;
    font-size: 11px;
  }
  .label--grey .volume { color: var(--ink-light); }
  .label--white .volume { color: var(--charcoal); }
</style>
</head>
<body>

  <section class="label label--grey">
    <div class="label__crimp"></div>
    <div class="label__foliage" role="img" aria-label="Faint botanical leaf pattern"></div>
    <div class="brand">
      <span class="brand__square"></span>
      <span class="brand__name">Dovelin</span>
    </div>
    <div class="title-band">
      <div class="title-band__stroke" role="img" aria-label="Black charcoal brush stroke"></div>
      <div class="title-band__text">
        <p class="title__eyebrow">ACTIVATED</p>
        <h1 class="title__main">BLACK<br>CHARCOAL</h1>
        <p class="title__sub">FACIAL WASH</p>
      </div>
    </div>
    <ul class="claims">
      <li>CLEANSE</li>
      <li>EXFOLIATE</li>
      <li>DETOX</li>
    </ul>
    <p class="volume">250ml</p>
  </section>

  <section class="label label--white">
    <div class="label__crimp"></div>
    <div class="label__foliage" role="img" aria-label="Faint botanical leaf pattern"></div>
    <div class="brand">
      <span class="brand__square"></span>
      <span class="brand__name">Dovelin</span>
    </div>
    <div class="title-band">
      <div class="title-band__stroke" role="img" aria-label="Black charcoal brush stroke"></div>
      <div class="title-band__text">
        <p class="title__eyebrow">ACTIVATED</p>
        <h1 class="title__main">BLACK<br>CHARCOAL</h1>
        <p class="title__sub">FACIAL WASH</p>
      </div>
    </div>
    <ul class="claims">
      <li>CLEANSE</li>
      <li>EXFOLIATE</li>
      <li>DETOX</li>
    </ul>
    <p class="volume">250ml</p>
  </section>

</body>
</html>
```